Business Card Design

WE are looking for a premium quality Business Cards for a Law Firm . Copies of our current business card is attached.
Updates

Went on vacation/holiday

Contact Information for Business Card

xyz

```html
<!DOCTYPE html>
<html lang="en">
<head>
<meta charset="UTF-8">
<title>Ashcombe Lawyers – Business Card</title>
<link rel="stylesheet" href="https://fonts.googleapis.com/css2?family=Montserrat:wght@400;500;600;700&display=swap">
<style>
  :root {
    --bg: #3a3a3a;
    --green: #0d2a1e;
    --green-deep: #062016;
    --green-light: #173d2c;
    --gold: #bf9a56;
    --white: #ffffff;
    --ink: #1c1c1c;
    --rule: #b9b9b9;
  }
  * { margin: 0; padding: 0; box-sizing: border-box; }
  html, body { width: 1200px; height: 1200px; overflow: hidden; }
  body {
    background: var(--bg);
    font-family: "Montserrat", sans-serif;
    display: flex; flex-direction: column; align-items: center; justify-content: center;
    gap: 44px;
  }
  .card {
    position: relative;
    width: 900px; height: 514px;
    border-radius: 36px;
    overflow: hidden;
    box-shadow: 0 14px 30px rgba(0,0,0,.35);
  }
  /* Front */
  .card-front { background: var(--white); }
  .front-bands { position: absolute; inset: 0; }
  .person { position: absolute; left: 70px; top: 92px; }
  .person-name { color: var(--gold); font-weight: 700; font-size: 42px; letter-spacing: 1px; line-height: 1; }
  .person-role { color: var(--ink); font-size: 14px; font-weight: 500; line-height: 1.2; margin-top: 8px; text-transform: uppercase; }
  .contact-list { list-style: none; margin-top: 26px; }
  .contact-list li { display: flex; align-items: center; gap: 14px; font-size: 17px; color: var(--ink); height: 38px; }
  .contact-icon { width: 28px; height: 28px; border-radius: 50%; background: var(--gold); display: flex; align-items: center; justify-content: center; flex: none; }
  .contact-icon svg { width: 15px; height: 15px; }
  .divider-v { position: absolute; left: 470px; top: 78px; width: 1px; height: 250px; background: var(--rule); }
  .firm-name { position: absolute; font-weight: 600; text-transform: uppercase; line-height: 1; white-space: nowrap; }
  .card-front .firm-name { left: 470px; right: 0; top: 188px; text-align: center; font-size: 28px; color: var(--green); }
  .office-address { position: absolute; right: 350px; top: 378px; text-align: right; font-size: 20px; color: var(--ink); line-height: 1.35; }
  /* Back */
  .card-back {
    background: radial-gradient(ellipse at 45% 70%, var(--green-light) 0%, var(--green) 40%, var(--green-deep) 100%);
  }
  .card-back .firm-name { left: 0; right: 0; top: 170px; text-align: center; font-size: 46px; color: var(--white); }
  .offices { position: absolute; left: 90px; right: 70px; bottom: 54px; display: flex; justify-content: space-between; align-items: flex-end; }
  .office { color: var(--white); font-size: 15px; line-height: 1.4; }
  .office-title { color: var(--gold); font-weight: 700; font-size: 15px; text-transform: uppercase; margin-bottom: 4px; }
  .office-row { display: flex; gap: 10px; align-items: flex-start; }
  .office-row svg { width: 16px; height: 16px; flex: none; margin-top: 2px; }
  .office-divider { width: 1px; height: 110px; background: rgba(191,154,86,.6); align-self: center; }
</style>
</head>
<body>

<section class="card card-front" aria-label="Business card front">
  <svg class="front-bands" viewBox="0 0 900 514" preserveAspectRatio="none" aria-hidden="true">
    <polygon points="0,490 560,450 560,514 0,514" fill="var(--gold)"/>
    <polygon points="574,444 900,300 900,514 574,514" fill="var(--green)"/>
  </svg>

  <div class="person">
    <h1 class="person-name">ROHAN MEHTA</h1>
    <p class="person-role">Director &amp; Principal Solicitor<br>MBA, Juris Doctor</p>
    <ul class="contact-list">
      <li><span class="contact-icon"><svg viewBox="0 0 24 24"><path fill="#fff" d="M6.6 10.8a15 15 0 0 0 6.6 6.6l2.2-2.2c.3-.3.7-.4 1-.2 1.1.4 2.3.6 3.6.6.6 0 1 .4 1 1V20c0 .6-.4 1-1 1A17 17 0 0 1 3 4c0-.6.4-1 1-1h3.5c.6 0 1 .4 1 1 0 1.3.2 2.5.6 3.6.1.3 0 .7-.2 1z"/></svg></span>+617 3555 0142</li>
      <li><span class="contact-icon"><svg viewBox="0 0 24 24"><rect x="7" y="2" width="10" height="20" rx="2" fill="none" stroke="#fff" stroke-width="2"/><circle cx="12" cy="18" r="1.2" fill="#fff"/></svg></span>+61 0400 555 218</li>
      <li><span class="contact-icon"><svg viewBox="0 0 24 24"><rect x="3" y="5" width="18" height="14" rx="1" fill="none" stroke="#fff" stroke-width="2"/><path d="M3 6l9 7 9-7" fill="none" stroke="#fff" stroke-width="2"/></svg></span>rohan@ashcombelawyers.com.au</li>
      <li><span class="contact-icon"><svg viewBox="0 0 24 24"><circle cx="12" cy="12" r="9" fill="none" stroke="#fff" stroke-width="2"/><ellipse cx="12" cy="12" rx="4" ry="9" fill="none" stroke="#fff" stroke-width="1.5"/><path d="M3 12h18" stroke="#fff" stroke-width="1.5"/></svg></span>www.ashcombelawyers.com.au</li>
    </ul>
  </div>

  <div class="divider-v"></div>

  <p class="firm-name">Ashcombe Lawyers</p>

  <p class="office-address">Level 4, Ashcombe House,<br>210 Harlow Terrace, Spring Hill, QLD 4000</p>
</section>

<section class="card card-back" aria-label="Business card back">
  <p class="firm-name">Ashcombe Lawyers</p>

  <div class="offices">
    <div class="office">
      <p class="office-title">Brisbane Office</p>
      <div class="office-row"><svg viewBox="0 0 24 24"><path fill="var(--gold)" d="M12 2a7 7 0 0 0-7 7c0 5 7 13 7 13s7-8 7-13a7 7 0 0 0-7-7zm0 9.5A2.5 2.5 0 1 1 12 6.5a2.5 2.5 0 0 1 0 5z"/></svg><span>Level 4, Ashcombe House, 210<br>Harlow Terrace Spring Hill QLD 4000</span></div>
      <div class="office-row"><svg viewBox="0 0 24 24"><path fill="var(--gold)" d="M6.6 10.8a15 15 0 0 0 6.6 6.6l2.2-2.2c.3-.3.7-.4 1-.2 1.1.4 2.3.6 3.6.6.6 0 1 .4 1 1V20c0 .6-.4 1-1 1A17 17 0 0 1 3 4c0-.6.4-1 1-1h3.5c.6 0 1 .4 1 1 0 1.3.2 2.5.6 3.6.1.3 0 .7-.2 1z"/></svg><span>(07) 3555 0142</span></div>
    </div>
    <div class="office-divider"></div>
    <div class="office">
      <p class="office-title">Melbourne Office</p>
      <div class="office-row"><svg viewBox="0 0 24 24"><path fill="var(--gold)" d="M12 2a7 7 0 0 0-7 7c0 5 7 13 7 13s7-8 7-13a7 7 0 0 0-7-7zm0 9.5A2.5 2.5 0 1 1 12 6.5a2.5 2.5 0 0 1 0 5z"/></svg><span>Suite 310, Larkin Chambers, 512<br>Elder Lane, Melbourne, VIC, 3000</span></div>
      <div class="office-row"><svg viewBox="0 0 24 24"><path fill="var(--gold)" d="M6.6 10.8a15 15 0 0 0 6.6 6.6l2.2-2.2c.3-.3.7-.4 1-.2 1.1.4 2.3.6 3.6.6.6 0 1 .4 1 1V20c0 .6-.4 1-1 1A17 17 0 0 1 3 4c0-.6.4-1 1-1h3.5c.6 0 1 .4 1 1 0 1.3.2 2.5.6 3.6.1.3 0 .7-.2 1z"/></svg><span>(07) 3555 0142</span></div>
    </div>
  </div>
</section>

</body>
</html>
```